vireLattice "organisation chart"

We need a new Organisation Chart for our Company! We are actually in a Change-management-process and will Change from a hierarchical Organisation in to a Network Organisation. Therefor we need a new Organisation Chart.
The following departements must be visible and legible on the Chart:
Team Sales & Consulting
Team Productmanagement
Team Supply Chain
Team Human Resources
Team Smart Digital Development
Team Marketing & Communication
The title of the Chart ist «vireLattice»
The Colors of the back of the Chart must be: RGB 73/25/102 // Pantone 2627
The Colors for the different Teams should be:
Team Sales & Consulting (Pantone: 803/neon yellow = Background)
Team Productmanagement (Pantone: 804/neon orange = Background)
Team Supply Chain (Pantone: 802/neon green = Background)
Team Human Resources (Pantone: 801/neon blue = Background)
Team Smart Digital Development (Pantone: 805/neon red = Background)
Team Marketing & Communication (Pantone: 803/neon pink = Background)
See below (upload files) an example showing a self-made Chart ... :-)
Our font is: Univers LT Std // Please feel free to Combine the Fonts Colors with the background colors
It Company

```html
<!DOCTYPE html>
<html lang="en">
<head>
<meta charset="utf-8">
<title>vireLattice – Organisation Chart</title>
<link rel="stylesheet" href="https://fonts.googleapis.com/css2?family=Fira+Sans+Extra+Condensed:wght@500&display=swap">
<style>
  :root {
    --bg: #491966;
    --ink: #4a1a63;
    --sales: #fdf575;
    --product: #ff7b1c;
    --supply: #33ff2a;
    --hr: #00aad8;
    --digital: #f72400;
    --marketing: #e46fb4;
    --core: #ffffff;
  }
  html, body {
    margin: 0;
    padding: 0;
    width: 1200px;
    height: 1200px;
    overflow: hidden;
    background: var(--bg);
  }
  .org-chart {
    display: block;
    width: 1200px;
    height: 1200px;
    font-family: "Fira Sans Extra Condensed", "Arial Narrow", sans-serif;
    font-weight: 500;
  }
  .segment--sales { fill: var(--sales); }
  .segment--product { fill: var(--product); }
  .segment--supply { fill: var(--supply); }
  .segment--hr { fill: var(--hr); }
  .segment--digital { fill: var(--digital); }
  .segment--marketing { fill: var(--marketing); }
  .divider { stroke: var(--bg); stroke-width: 32; }
  .core-halo { fill: var(--bg); opacity: 0.35; }
  .core { fill: var(--core); }
  .link-arrow { fill: none; stroke: var(--bg); stroke-width: 17; }
  .arrow-head { fill: var(--bg); }
  .team-label { fill: var(--ink); font-size: 36px; text-anchor: middle; dominant-baseline: middle; }
  .title { fill: var(--ink); font-size: 64px; text-anchor: middle; dominant-baseline: middle; }
</style>
</head>
<body>
<svg class="org-chart" viewBox="0 0 1200 1200" role="img" aria-label="vireLattice network organisation chart">
  <defs>
    <marker id="arrowhead" viewBox="0 0 10 10" refX="3" refY="5" markerUnits="userSpaceOnUse" markerWidth="54" markerHeight="54" orient="auto-start-reverse">
      <path class="arrow-head" d="M0,0 L10,5 L0,10 z"/>
    </marker>
  </defs>

  <rect width="1200" height="1200" fill="var(--bg)"/>

  <g class="segments">
    <path class="segment--product" d="M600,600 L600,155 A445,445 0 0 1 985.4,377.5 Z"/>
    <path class="segment--supply" d="M600,600 L985.4,377.5 A445,445 0 0 1 985.4,822.5 Z"/>
    <path class="segment--hr" d="M600,600 L985.4,822.5 A445,445 0 0 1 600,1045 Z"/>
    <path class="segment--digital" d="M600,600 L600,1045 A445,445 0 0 1 214.6,822.5 Z"/>
    <path class="segment--marketing" d="M600,600 L214.6,822.5 A445,445 0 0 1 214.6,377.5 Z"/>
    <path class="segment--sales" d="M600,600 L214.6,377.5 A445,445 0 0 1 600,155 Z"/>
  </g>

  <g class="dividers">
    <line class="divider" x1="600" y1="600" x2="600" y2="140"/>
    <line class="divider" x1="600" y1="600" x2="600" y2="1060"/>
    <line class="divider" x1="600" y1="600" x2="998" y2="370"/>
    <line class="divider" x1="600" y1="600" x2="998" y2="830"/>
    <line class="divider" x1="600" y1="600" x2="202" y2="370"/>
    <line class="divider" x1="600" y1="600" x2="202" y2="830"/>
  </g>

  <g class="links">
    <path class="link-arrow" marker-start="url(#arrowhead)" marker-end="url(#arrowhead)" d="M512,199 A410,410 0 0 1 688,199"/>
    <path class="link-arrow" marker-start="url(#arrowhead)" marker-end="url(#arrowhead)" d="M896,317 A410,410 0 0 1 984,469"/>
    <path class="link-arrow" marker-start="url(#arrowhead)" marker-end="url(#arrowhead)" d="M984,731 A410,410 0 0 1 896,883"/>
    <path class="link-arrow" marker-start="url(#arrowhead)" marker-end="url(#arrowhead)" d="M688,1001 A410,410 0 0 1 512,1001"/>
    <path class="link-arrow" marker-start="url(#arrowhead)" marker-end="url(#arrowhead)" d="M304,883 A410,410 0 0 1 216,731"/>
    <path class="link-arrow" marker-start="url(#arrowhead)" marker-end="url(#arrowhead)" d="M216,469 A410,410 0 0 1 304,317"/>
  </g>

  <circle class="core-halo" cx="600" cy="600" r="194"/>
  <circle class="core" cx="600" cy="600" r="180"/>

  <text class="title" x="600" y="602">vireLattice</text>

  <text class="team-label">
    <tspan x="438" y="278">Team</tspan>
    <tspan x="438" y="323">Sales &amp;</tspan>
    <tspan x="438" y="369">Consulting</tspan>
  </text>
  <text class="team-label">
    <tspan x="759" y="278">Team</tspan>
    <tspan x="759" y="323">Product</tspan>
    <tspan x="759" y="369">Management</tspan>
  </text>
  <text class="team-label">
    <tspan x="902" y="555">Team</tspan>
    <tspan x="902" y="600">Supply</tspan>
    <tspan x="902" y="646">Chain</tspan>
  </text>
  <text class="team-label">
    <tspan x="768" y="831">Team</tspan>
    <tspan x="768" y="877">Human</tspan>
    <tspan x="768" y="922">Resources</tspan>
  </text>
  <text class="team-label">
    <tspan x="437" y="831">Team</tspan>
    <tspan x="437" y="877">Smart Digital</tspan>
    <tspan x="437" y="922">Development</tspan>
  </text>
  <text class="team-label">
    <tspan x="287" y="555">Team</tspan>
    <tspan x="287" y="600">Marketing &amp;</tspan>
    <tspan x="287" y="646">Communication</tspan>
  </text>
</svg>
</body>
</html>
```